Powerful Design & Selling Tool

We sell health care consulting Services to medical practices (doctors).<br/>we need a powerful design to use as a selling tool that conveys, health care knowledge, expertise professionalism and includes the services we offer. <br/>The design should incorporate our logo and its colors (blue and white). However other colors can be included. I am open to the designer's creativity and color options. you can find our logo on our website at www bright harbor advisory.com. Please feel free to ask questions.

Target Market(s)

Doctors and health care administrators

Industry/Entity Type

Health Care

Colors

Designer to choose colors to be used in the design.

Requirements
Must have
• logo somewhere in the footer
Nice to have
• any creative designs the design wants to add

```html
<!DOCTYPE html>
<html lang="en">
<head>
<meta charset="utf-8">
<title>Bright Harbor Advisory – Presentation Template</title>
<link href="https://fonts.googleapis.com/css2?family=Montserrat:wght@300;400;600;700&family=Open+Sans:ital,wght@0,400;0,600;0,700;1,400&display=swap" rel="stylesheet">
<style>
:root{
  --blue:#0b48a6;
  --navy:#0a2a94;
  --deep:#0c2f8c;
  --dark:#3b3b3b;
  --bar-grey:#8a8a8a;
  --box-grey:#d4d4d4;
  --pale:#e6ebf3;
  --ink:#4a4a4a;
  --muted:#8a8a8a;
  --white:#ffffff;
}
*{margin:0;padding:0;box-sizing:border-box}
html,body{width:1200px;height:1200px;overflow:hidden;background:#000}
body{position:relative;font-family:'Open Sans',sans-serif}
.slide{position:absolute;width:372px;height:278px;background:var(--white);overflow:hidden}
.abs{position:absolute}
.header{position:absolute;left:0;top:0;width:100%;height:24px;background:var(--blue);color:var(--white);
  font:600 11px/24px 'Montserrat',sans-serif;padding-left:7px}
.header::after{content:"";position:absolute;left:8px;bottom:-5px;border-left:5px solid transparent;border-right:5px solid transparent;border-top:5px solid var(--blue)}
.footer{position:absolute;left:0;bottom:0;width:372px;height:22px}
.copyright{position:absolute;left:6px;bottom:5px;color:var(--white);font:600 4.6px 'Open Sans',sans-serif}
.brand{position:absolute;right:8px;bottom:4px;color:var(--navy);font:600 5.5px 'Montserrat',sans-serif;white-space:nowrap}
.fine{font:400 4px/5.6px 'Open Sans',sans-serif;color:var(--muted)}
.sub-title{font:600 8.5px 'Montserrat',sans-serif;color:var(--blue)}
.photo{position:absolute}
.icon-ring{position:absolute;border-radius:50%;background:var(--blue);border:1.5px solid var(--white);box-shadow:0 0 0 1.5px var(--blue);display:flex;align-items:center;justify-content:center}
.col-text{position:absolute;width:84px;text-align:center}
.col-text .t{font:600 7px 'Open Sans',sans-serif;color:var(--blue)}
.col-text .d{font:400 4.8px/8.6px 'Open Sans',sans-serif;color:#444}
table{border-collapse:collapse}
</style>
</head>
<body>

<!-- Slide 1: cover -->
<section class="slide" style="left:22px;top:22px">
  <div class="photo" role="img" aria-label="Photo of medical professionals meeting in a bright office" style="left:0;top:0;width:372px;height:134px;background:linear-gradient(180deg,#c9ced4 0%,#a9afb6 45%,#6d6c70 100%)"></div>
  <div class="abs" style="left:0;top:134px;width:372px;height:24px;background:var(--blue);color:#fff;font:700 7.6px/24px 'Montserrat',sans-serif;text-align:center">EXPERTIES YOUR MEDICAL PRACTICE DESERVES</div>
  <div class="abs" style="left:181px;top:158px;border-left:5px solid transparent;border-right:5px solid transparent;border-top:5px solid var(--blue)"></div>
  <div class="abs" style="left:0;top:176px;width:372px;text-align:center;font:600 14px 'Montserrat',sans-serif;color:var(--blue)">Project Title goes here</div>
  <div class="abs" style="left:0;top:197px;width:372px;text-align:center;font:600 8.5px 'Montserrat',sans-serif;color:var(--blue)">Project Subtitle goes here</div>
  <div class="abs" style="left:0;top:226px;width:372px;text-align:center;font:600 9px 'Montserrat',sans-serif;color:var(--navy)">Bright Harbor Advisory</div>
  <div class="abs" style="left:0;bottom:0;width:372px;height:7px;background:#b5b5b5"></div>
</section>

<!-- Slide 2: paragraphs with image -->
<section class="slide" style="left:403px;top:22px">
  <div class="header">Project Title goes here</div>
  <div class="photo" role="img" aria-label="Photo of a smiling doctor in a white coat with colleagues" style="left:6px;top:41px;width:167px;height:204px;background:linear-gradient(180deg,#e4e6ea 0%,#cfd3d8 50%,#a7adb4 100%)"></div>
  <div class="abs" style="left:6px;top:206px;width:167px;height:39px;background:rgba(11,72,166,.85);color:#fff;font:italic 400 6px/11px 'Open Sans',sans-serif;padding:6px 8px">consectetuer adipiscing elit, sed orem ipsum dolor sit amet, consectetuer adipiscing elit, sed</div>
  <div class="abs sub-title" style="left:185px;top:45px;font-size:9.5px">Paragraphs Title here</div>
  <div class="abs fine" style="left:185px;top:63px;width:178px">orem ipsum dolor sit amet, consectetuer adipiscing elit, sed orem ipsum</div>
  <div class="abs fine" style="left:185px;top:78px;width:178px">Lorem ipsum dolor sit amet, consectetur adipiscing elit, sed diam nonummy nibh euismod tincidunt ut laoreet dolore magna aliquam erat volutpat. Lorem ipsum dolor sit amet, consectetur adipiscing elit, sed diam nonummy nibh euismod tincidunt ut laoreet dolore magna aliquam erat volutpat. Lorem ipsum dolor sit amet, consectetur adipiscing elit, sed diam nonummy nibh euismod tincidunt ut laoreet dolore magna aliquam erat volutpat.</div>
  <div class="abs fine" style="left:185px;top:130px;width:178px">Lorem ipsum dolor sit amet, consectetur adipiscing elit, sed diam nonummy nibh euismod tincidunt ut laoreet dolore magna aliquam erat volutpat. Lorem ipsum dolor sit amet, consectetur adipiscing elit, sed diam nonummy nibh euismod tincidunt ut laoreet dolore magna aliquam erat volutpat. Lorem ipsum dolor sit amet, consectetur adipiscing elit, sed diam nonummy nibh euismod tincidunt ut laoreet dolore magna aliquam erat volutpat.</div>
  <div class="abs fine" style="left:185px;top:202px;width:178px">Lorem ipsum dolor sit amet, consectetur adipiscing elit, sed diam nonummy nibh euismod tincidunt ut laoreet dolore magna aliquam erat volutpat. Lorem ipsum dolor sit amet, consectetur adipiscing elit, sed diam nonummy nibh euismod tincidunt ut laoreet dolore magna aliquam erat volutpat. Lorem ipsum dolor sit amet, consectetur adipiscing elit, sed diam nonummy nibh euismod tincidunt.</div>
  <svg class="footer" viewBox="0 0 372 22"><rect y="2" width="372" height="20" fill="#3b3b3b"/><path d="M200 22C240 6 290 2 372 2V22Z" fill="#fff"/><path d="M200 22C240 6 290 2 372 2V5C300 5 250 10 218 22Z" fill="#0b48a6"/></svg>
  <div class="copyright">Copyright text here</div>
  <div class="brand">Bright Harbor Advisory</div>
</section>

<!-- Slide 3: A B C -->
<section class="slide" style="left:790px;top:22px">
  <div class="header">Project Title goes here</div>
  <div class="abs fine" style="left:20px;top:54px;width:332px;text-align:center">Lorem ipsum dolor sit amet, consectetur adipiscing elit, sed diam nonummy nibh euismod tincidunt ut laoreet dolore magna aliquam erat volutpat. Lorem ipsum dolor sit amet, consectetur adipiscing elit, sed diam nonummy nibh euismod tincidunt ut laoreet dolore magna aliquam erat volutpat. Lorem ipsum dolor sit amet, consectetur adipiscing elit, sed diam nonummy nibh euismod tincidunt ut laoreet dolore magna aliquam erat volutpat.</div>
  <div class="abs" style="left:25px;top:111px;width:92px;height:66px;background:var(--box-grey)"></div>
  <div class="abs" style="left:141px;top:111px;width:92px;height:66px;background:var(--box-grey)"></div>
  <div class="abs" style="left:257px;top:111px;width:92px;height:66px;background:var(--box-grey)"></div>
  <div class="icon-ring" style="left:63px;top:170px;width:16px;height:16px;color:#fff;font:600 8px 'Montserrat',sans-serif">A</div>
  <div class="icon-ring" style="left:179px;top:170px;width:16px;height:16px;color:#fff;font:600 8px 'Montserrat',sans-serif">B</div>
  <div class="icon-ring" style="left:295px;top:170px;width:16px;height:16px;color:#fff;font:600 8px 'Montserrat',sans-serif">C</div>
  <div class="abs" style="left:25px;top:193px;width:92px;text-align:center;font:italic 600 5px 'Open Sans',sans-serif;color:#333">Lorem Ipsum</div>
  <div class="abs" style="left:141px;top:193px;width:92px;text-align:center;font:italic 600 5px 'Open Sans',sans-serif;color:#333">Lorem Ipsum</div>
  <div class="abs" style="left:257px;top:193px;width:92px;text-align:center;font:italic 600 5px 'Open Sans',sans-serif;color:#333">Lorem Ipsum</div>
  <div class="abs fine" style="left:41px;top:202px;width:60px;text-align:center">Lorem ipsum dolor sit amet, consectetuer adipiscing elit, sed diam nonummy nibh</div>
  <div class="abs fine" style="left:157px;top:202px;width:60px;text-align:center">Lorem ipsum dolor sit amet, consectetuer adipiscing elit, sed diam nonummy nibh</div>
  <div class="abs fine" style="left:273px;top:202px;width:60px;text-align:center">Lorem ipsum dolor sit amet, consectetuer adipiscing elit, sed diam nonummy nibh</div>
  <svg class="footer" viewBox="0 0 372 22"><rect y="2" width="372" height="20" fill="#3b3b3b"/><path d="M200 22C240 6 290 2 372 2V22Z" fill="#fff"/><path d="M200 22C240 6 290 2 372 2V5C300 5 250 10 218 22Z" fill="#0b48a6"/></svg>
  <div class="copyright">Copyright text here</div>
  <div class="brand">Bright Harbor Advisory</div>
</section>

<!-- Slide 4: tables -->
<section class="slide" style="left:22px;top:317px">
  <div class="header">Project Title goes here</div>
  <div class="abs" style="left:7px;top:35px;font:400 7px 'Open Sans',sans-serif;color:#777">Table Style 2</div>
  <table class="abs" style="left:8px;top:47px;width:353px;font:400 6.6px 'Open Sans',sans-serif;color:#444">
    <tr style="background:var(--bar-grey);color:#fff;font-weight:600;height:14px"><td style="padding-left:14px">Title 1</td><td>Title 2</td><td>Title 3</td><td>Title 4</td><td>Title 5</td><td>Title 6</td></tr>
    <tr style="height:15px"><td style="padding-left:10px;padding-top:4px">Lorem ipsum dolor</td><td>xxx</td><td>xxx</td><td>xxx</td><td>xxx</td><td>xxx</td></tr>
    <tr style="height:15px"><td style="padding-left:10px">Lorem ipsum dolor</td><td>xxx</td><td>xxx</td><td>xxx</td><td>xxx</td><td>xxx</td></tr>
    <tr style="height:15px"><td style="padding-left:10px">Lorem ipsum dolor</td><td>xxx</td><td>xxx</td><td>xxx</td><td>xxx</td><td>xxx</td></tr>
    <tr style="height:15px"><td style="padding-left:10px">Lorem ipsum dolor</td><td>xxx</td><td>xxx</td><td>xxx</td><td>xxx</td><td>xxx</td></tr>
  </table>
  <div class="abs" style="left:7px;top:146px;font:600 7px 'Open Sans',sans-serif;color:var(--blue)">Table Style 2</div>
  <table class="abs" style="left:8px;top:158px;width:353px;font:400 6.6px 'Open Sans',sans-serif;color:#444;outline:1px solid var(--blue)">
    <tr style="background:var(--blue);color:#fff;font-weight:600;height:14px"><td style="padding-left:14px">Title 1</td><td>Title 2</td><td>Title 3</td><td>Title 4</td><td>Title 5</td><td>Title 6</td></tr>
    <tr style="height:15px"><td style="padding-left:10px;padding-top:4px">Lorem ipsum dolor</td><td>xxx</td><td>xxx</td><td>xxx</td><td>xxx</td><td>xxx</td></tr>
    <tr style="height:15px"><td style="padding-left:10px">Lorem ipsum dolor</td><td>xxx</td><td>xxx</td><td>xxx</td><td>xxx</td><td>xxx</td></tr>
    <tr style="height:15px"><td style="padding-left:10px">Lorem ipsum dolor</td><td>xxx</td><td>xxx</td><td>xxx</td><td>xxx</td><td>xxx</td></tr>
    <tr style="height:15px"><td style="padding-left:10px">Lorem ipsum dolor</td><td>xxx</td><td>xxx</td><td>xxx</td><td>xxx</td><td>xxx</td></tr>
  </table>
  <svg class="footer" viewBox="0 0 372 22"><rect y="2" width="372" height="20" fill="#3b3b3b"/><path d="M200 22C240 6 290 2 372 2V22Z" fill="#fff"/><path d="M200 22C240 6 290 2 372 2V5C300 5 250 10 218 22Z" fill="#0b48a6"/></svg>
  <div class="copyright">Copyright text here</div>
  <div class="brand">Bright Harbor Advisory</div>
</section>

<!-- Slide 5: graphs -->
<section class="slide" style="left:403px;top:317px">
  <div class="header">Project Title goes here</div>
  <div class="abs sub-title" style="left:10px;top:45px;font-size:8.5px">Graphs Title Here</div>
  <div class="abs" style="left:10px;top:57px;width:330px;font:400 5px/9px 'Open Sans',sans-serif;color:var(--muted)">amet, consectetuer amet, consectetuer amet, consect etuer amet, consectetuer amet, consectetuer amet, consectetuer amet, consectetuer amet, consectetuer amet, consectetuer amet, consectetuer amet, consectetuer amet, consectetuer amet, consectetuer amet, consectetuer amet, consectetuer amet, consectetuer amet.</div>
  <svg class="abs" style="left:0;top:98px" width="230" height="110" viewBox="0 0 230 110" font-family="Open Sans, sans-serif" font-size="4.5" fill="#777">
    <g stroke="#e2e2e2" stroke-width=".6">
      <line x1="30" y1="7" x2="215" y2="7"/><line x1="30" y1="21.7" x2="215" y2="21.7"/><line x1="30" y1="36.3" x2="215" y2="36.3"/><line x1="30" y1="51" x2="215" y2="51"/><line x1="30" y1="65.7" x2="215" y2="65.7"/><line x1="30" y1="80.3" x2="215" y2="80.3"/><line x1="30" y1="95" x2="215" y2="95"/>
    </g>
    <text x="17" y="9">600</text><text x="17" y="23.5">500</text><text x="17" y="38">400</text><text x="17" y="53">300</text><text x="17" y="67.5">200</text><text x="17" y="82">100</text><text x="22" y="97">0</text>
    <rect x="35" y="55.4" width="8" height="39.6" fill="#0b2fd0"/><rect x="43" y="65.7" width="8" height="29.3" fill="#1c1c1c"/>
    <rect x="74" y="30.5" width="8" height="64.5" fill="#0b2fd0"/><rect x="82" y="39.3" width="8" height="55.7" fill="#1c1c1c"/>
    <rect x="113" y="55.4" width="8" height="39.6" fill="#0b2fd0"/><rect x="121" y="46.6" width="8" height="48.4" fill="#1c1c1c"/>
    <rect x="152" y="49.5" width="8" height="45.5" fill="#0b2fd0"/><rect x="160" y="55.4" width="8" height="39.6" fill="#1c1c1c"/>
    <rect x="191" y="29" width="8" height="66" fill="#0b2fd0"/><rect x="199" y="33.4" width="8" height="61.6" fill="#1c1c1c"/>
    <text x="39" y="106">JAN</text><text x="78" y="106">APR</text><text x="118" y="106">JUL</text><text x="156" y="106">OCT</text><text x="195" y="106">DEC</text>
  </svg>
  <svg class="abs" style="left:240px;top:117px" width="40" height="86" viewBox="0 0 40 86" font-family="Open Sans, sans-serif" font-style="italic" font-size="6" fill="#555">
    <circle cx="18" cy="18" r="14" fill="none" stroke="#e4e4e4" stroke-width="3"/>
    <circle cx="18" cy="18" r="14" fill="none" stroke="#0b2fd0" stroke-width="3" stroke-dasharray="66 88" transform="rotate(-90 18 18)"/>
    <text x="18" y="20" text-anchor="middle">75%</text>
    <circle cx="18" cy="64" r="14" fill="none" stroke="#e4e4e4" stroke-width="3"/>
    <circle cx="18" cy="64" r="14" fill="none" stroke="#111" stroke-width="3" stroke-dasharray="53 88" transform="rotate(-90 18 64)"/>
    <text x="18" y="66" text-anchor="middle">60%</text>
  </svg>
  <div class="abs" style="left:280px;top:121px;font:italic 600 6px 'Open Sans',sans-serif;color:#222">Lorem Ipsum</div>
  <div class="abs fine" style="left:280px;top:129px;width:72px">Lorem ipsum dolor sit amet, consectetuer adipiscing elit, sed diam nonummy nibh</div>
  <div class="abs" style="left:280px;top:167px;font:italic 600 6px 'Open Sans',sans-serif;color:#222">Lorem Ipsum</div>
  <div class="abs fine" style="left:280px;top:175px;width:72px">Lorem ipsum dolor sit amet, consectetuer adipiscing elit, sed diam nonummy nibh</div>
  <svg class="footer" viewBox="0 0 372 22"><rect y="2" width="372" height="20" fill="#3b3b3b"/><path d="M200 22C240 6 290 2 372 2V22Z" fill="#fff"/><path d="M200 22C240 6 290 2 372 2V5C300 5 250 10 218 22Z" fill="#0b48a6"/></svg>
  <div class="copyright">Copyright text here</div>
  <div class="brand">Bright Harbor Advisory</div>
</section>

<!-- Slide 6: timeline -->
<section class="slide" style="left:790px;top:317px">
  <div class="header">Project Title goes here</div>
  <svg class="abs" style="left:0;top:0" width="372" height="250" viewBox="0 0 372 250" font-family="Montserrat, sans-serif" font-weight="600" font-size="11" fill="#fff" text-anchor="middle">
    <g fill="none" stroke="#0b2fa0" stroke-width="1.2" stroke-dasharray="1 1.6">
      <circle cx="51" cy="163" r="33"/><circle cx="118" cy="119" r="33"/><circle cx="186" cy="163" r="33"/><circle cx="253" cy="119" r="33"/><circle cx="320" cy="163" r="33"/>
    </g>
    <g fill="#0b2fa0">
      <circle cx="51" cy="163" r="27"/><circle cx="118" cy="119" r="27"/><circle cx="186" cy="163" r="27"/><circle cx="253" cy="119" r="27"/><circle cx="320" cy="163" r="27"/>
    </g>
    <text x="51" y="167">2014</text><text x="118" y="123">2015</text><text x="186" y="167">2016</text><text x="253" y="123">2017</text><text x="320" y="167">2018</text>
  </svg>
  <div class="abs" style="left:16px;top:75px;width:70px;text-align:center"><div style="font:600 5.5px 'Montserrat',sans-serif;color:var(--blue)">Icon Title here</div><div class="fine" style="margin-top:1px">amet, consectetuer amet, consectetuer amet, consectetuer amet, consectetuer amet, consectetuer amet, consectetuer amet, consectetuer amet.</div></div>
  <div class="abs" style="left:151px;top:75px;width:70px;text-align:center"><div style="font:600 5.5px 'Montserrat',sans-serif;color:var(--blue)">Icon Title here</div><div class="fine" style="margin-top:1px">amet, consectetuer amet, consectetuer amet, consectetuer amet, consectetuer amet, consectetuer amet, consectetuer amet, consectetuer amet.</div></div>
  <div class="abs" style="left:288px;top:75px;width:70px;text-align:center"><div style="font:600 5.5px 'Montserrat',sans-serif;color:var(--blue)">Icon Title here</div><div class="fine" style="margin-top:1px">amet, consectetuer amet, consectetuer amet, consectetuer amet, consectetuer amet, consectetuer amet, consectetuer amet, consectetuer amet.</div></div>
  <div class="abs" style="left:83px;top:155px;width:70px;text-align:center"><div style="font:600 5.5px 'Montserrat',sans-serif;color:var(--blue)">Icon Title here</div><div class="fine" style="margin-top:1px">amet, consectetuer amet, consectetuer amet, consectetuer amet, consectetuer amet, consectetuer amet, consectetuer amet, consectetuer amet.</div></div>
  <div class="abs" style="left:218px;top:155px;width:70px;text-align:center"><div style="font:600 5.5px 'Montserrat',sans-serif;color:var(--blue)">Icon Title here</div><div class="fine" style="margin-top:1px">amet, consectetuer amet, consectetuer amet, consectetuer amet, consectetuer amet, consectetuer amet, consectetuer amet, consectetuer amet.</div></div>
  <svg class="footer" viewBox="0 0 372 22"><rect y="2" width="372" height="20" fill="#3b3b3b"/><path d="M200 22C240 6 290 2 372 2V22Z" fill="#fff"/><path d="M200 22C240 6 290 2 372 2V5C300 5 250 10 218 22Z" fill="#0b48a6"/></svg>
  <div class="copyright">Copyright text here</div>
  <div class="brand">Bright Harbor Advisory</div>
</section>

<!-- Slide 7: image + icon list -->
<section class="slide" style="left:22px;top:603px">
  <div class="header">Project Title goes here</div>
  <div class="photo" role="img" aria-label="Photo of two colleagues reviewing work on a laptop in an office" style="left:0;top:24px;width:178px;height:232px;background:linear-gradient(160deg,#d6dbe0 0%,#aeb4b9 45%,#7a6d60 100%)"></div>
  <div class="abs" style="left:178px;top:24px;width:194px;height:232px;background:var(--deep)"></div>
  <div class="icon-ring" style="left:165px;top:41px;width:34px;height:34px"><svg width="14" height="14" viewBox="0 0 14 14" fill="none" stroke="#fff" stroke-width="1"><circle cx="7" cy="7" r="5.5"/><path d="M4 7h6M7 4v6"/></svg></div>
  <div class="icon-ring" style="left:165px;top:93px;width:34px;height:34px"><svg width="14" height="14" viewBox="0 0 14 14" fill="none" stroke="#fff" stroke-width="1"><rect x="2" y="3" width="10" height="8"/><path d="M4 6h6M4 8h4"/></svg></div>
  <div class="icon-ring" style="left:165px;top:146px;width:34px;height:34px"><svg width="14" height="14" viewBox="0 0 14 14" fill="none" stroke="#fff" stroke-width="1"><rect x="3" y="2" width="8" height="10"/><path d="M5 5h4M5 7h4M5 9h3"/></svg></div>
  <div class="icon-ring" style="left:165px;top:201px;width:34px;height:34px"><svg width="14" height="14" viewBox="0 0 14 14" fill="none" stroke="#fff" stroke-width="1"><circle cx="4" cy="5" r="1.5"/><circle cx="10" cy="5" r="1.5"/><circle cx="7" cy="4" r="1.5"/><path d="M2 11v-2h10v2"/></svg></div>
  <div class="abs" style="left:207px;top:46px;width:160px;color:#fff"><div style="font:600 7.5px 'Open Sans',sans-serif">Icon Title hrere</div><div style="font:400 5.2px/9.6px 'Open Sans',sans-serif">consectetur adipiscing elit, sed do eiusmod tempor incididunt ut labore et dolore magna aliqua. Ut enim ad minim veniam</div></div>
  <div class="abs" style="left:207px;top:97px;width:160px;color:#fff"><div style="font:600 7.5px 'Open Sans',sans-serif">Icon Title hrere</div><div style="font:400 5.2px/9.6px 'Open Sans',sans-serif">consectetur adipiscing elit, sed do eiusmod tempor incididunt ut labore et dolore magna aliqua. Ut enim ad minim veniam</div></div>
  <div class="abs" style="left:207px;top:150px;width:160px;color:#fff"><div style="font:600 7.5px 'Open Sans',sans-serif">Icon Title hrere</div><div style="font:400 5.2px/9.6px 'Open Sans',sans-serif">consectetur adipiscing elit, sed do eiusmod tempor incididunt ut labore et dolore magna aliqua. Ut enim ad minim veniam</div></div>
  <div class="abs" style="left:207px;top:208px;width:160px;color:#fff"><div style="font:600 7.5px 'Open Sans',sans-serif">Icon Title hrere</div><div style="font:400 5.2px/9.6px 'Open Sans',sans-serif">consectetur adipiscing elit, sed do eiusmod tempor incididunt ut labore et dolore magna aliqua. Ut enim ad minim veniam</div></div>
  <svg class="footer" viewBox="0 0 372 22"><rect y="2" width="372" height="20" fill="#3b3b3b"/><path d="M200 22C240 6 290 2 372 2V22Z" fill="#fff"/><path d="M200 22C240 6 290 2 372 2V5C300 5 250 10 218 22Z" fill="#0b48a6"/></svg>
  <div class="copyright">Copyright text here</div>
  <div class="brand">Bright Harbor Advisory</div>
</section>

<!-- Slide 8: image + four icons -->
<section class="slide" style="left:403px;top:603px">
  <div class="header">Project Title goes here</div>
  <div class="photo" role="img" aria-label="Photo of two colleagues working on laptops at a meeting table" style="left:0;top:24px;width:372px;height:150px;background:linear-gradient(170deg,#d9dde2 0%,#b0b5ba 50%,#8d7d6c 100%)"></div>
  <div class="icon-ring" style="left:44px;top:158px;width:34px;height:34px"><svg width="14" height="14" viewBox="0 0 14 14" fill="none" stroke="#fff" stroke-width="1"><circle cx="7" cy="7" r="5.5"/><path d="M4 7h6M7 4v6"/></svg></div>
  <div class="icon-ring" style="left:129px;top:158px;width:34px;height:34px"><svg width="14" height="14" viewBox="0 0 14 14" fill="none" stroke="#fff" stroke-width="1"><rect x="2" y="3" width="10" height="8"/><path d="M4 6h6M4 8h4"/></svg></div>
  <div class="icon-ring" style="left:225px;top:158px;width:34px;height:34px"><svg width="14" height="14" viewBox="0 0 14 14" fill="none" stroke="#fff" stroke-width="1"><rect x="3" y="2" width="8" height="10"/><path d="M5 5h4M5 7h4M5 9h3"/></svg></div>
  <div class="icon-ring" style="left:309px;top:158px;width:34px;height:34px"><svg width="14" height="14" viewBox="0 0 14 14" fill="none" stroke="#fff" stroke-width="1"><circle cx="4" cy="5" r="1.5"/><circle cx="10" cy="5" r="1.5"/><circle cx="7" cy="4" r="1.5"/><path d="M2 11v-2h10v2"/></svg></div>
  <div class="col-text" style="left:19px;top:200px"><div class="t">Icon Title hrere</div><div class="d">consectetur adipiscing elit, sed do eiusmod tempor incididunt ut labore et dolore magna aliqua. Ut</div></div>
  <div class="col-text" style="left:104px;top:200px"><div class="t">Icon Title hrere</div><div class="d">consectetur adipiscing elit, sed do eiusmod tempor incididunt ut labore et dolore magna aliqua. Ut</div></div>
  <div class="col-text" style="left:200px;top:200px"><div class="t">Icon Title hrere</div><div class="d">consectetur adipiscing elit, sed do eiusmod tempor incididunt ut labore et dolore magna aliqua. Ut</div></div>
  <div class="col-text" style="left:284px;top:200px"><div class="t">Icon Title hrere</div><div class="d">consectetur adipiscing elit, sed do eiusmod tempor incididunt ut labore et dolore magna aliqua. Ut</div></div>
  <svg class="footer" viewBox="0 0 372 22"><rect y="2" width="372" height="20" fill="#3b3b3b"/><path d="M200 22C240 6 290 2 372 2V22Z" fill="#fff"/><path d="M200 22C240 6 290 2 372 2V5C300 5 250 10 218 22Z" fill="#0b48a6"/></svg>
  <div class="copyright">Copyright text here</div>
  <div class="brand">Bright Harbor Advisory</div>
</section>

<!-- Slide 9: services band -->
<section class="slide" style="left:790px;top:603px">
  <div class="header">Project Title goes here</div>
  <div class="abs fine" style="left:10px;top:45px;width:350px">Lorem ipsum dolor sit amet, consectetur adipiscing elit, sed diam nonummy nibh euismod tincidunt ut laoreet dolore magna aliquam erat volutpat. Lorem ipsum dolor sit amet, consectetur adipiscing elit, sed diam nonummy nibh euismod tincidunt ut laoreet dolore magna aliquam erat volutpat. Lorem ipsum dolor sit amet, consectetur adipiscing elit, sed diam nonummy nibh euismod tincidunt ut laoreet dolore magna aliquam erat volutpat.</div>
  <div class="abs" style="left:0;top:95px;width:366px;height:90px;background:var(--navy);border-radius:0 45px 45px 0"></div>
  <svg class="abs" style="left:0;top:101px" width="372" height="30" viewBox="0 0 372 30" fill="none" stroke="#fff" stroke-width="2.2">
    <path d="M36 8a11 11 0 1 1-3 8"/><path d="M35 4l1 5-5 0"/>
    <circle cx="136" cy="10" r="4"/><path d="M126 20l6 6h8l6-6"/><path d="M136 3v-2M136 19v-2"/>
    <rect x="217" y="3" width="13" height="18"/><path d="M220 12l3 3 5-6"/>
    <path d="M298 15h16v12h-16z"/><path d="M302 15v-4h8v4"/><circle cx="306" cy="6" r="3"/>
  </svg>
  <div class="abs" style="left:4px;top:138px;width:80px;text-align:center;color:#fff"><div style="font:700 6.4px 'Open Sans',sans-serif">Revenue Cycle</div><div style="font:400 4.8px/6.4px 'Open Sans',sans-serif;margin-top:2px">x ea commodo consequat. Duis autem x ea commodo consequat. Duis autem x ea commodo consequat.</div></div>
  <div class="abs" style="left:96px;top:138px;width:80px;text-align:center;color:#fff"><div style="font:700 6.4px 'Open Sans',sans-serif">Revenue Cycle</div><div style="font:400 4.8px/6.4px 'Open Sans',sans-serif;margin-top:2px">x ea commodo consequat. Duis autem x ea commodo consequat. Duis autem x ea commodo consequat.</div></div>
  <div class="abs" style="left:184px;top:138px;width:80px;text-align:center;color:#fff"><div style="font:700 6.4px 'Open Sans',sans-serif">Revenue Cycle</div><div style="font:400 4.8px/6.4px 'Open Sans',sans-serif;margin-top:2px">x ea commodo consequat. Duis autem x ea commodo consequat. Duis autem x ea commodo consequat.</div></div>
  <div class="abs" style="left:266px;top:138px;width:80px;text-align:center;color:#fff"><div style="font:700 6.4px 'Open Sans',sans-serif">Revenue Cycle</div><div style="font:400 4.8px/6.4px 'Open Sans',sans-serif;margin-top:2px">x ea commodo consequat. Duis autem x ea commodo consequat. Duis autem x ea commodo consequat.</div></div>
  <div class="abs fine" style="left:10px;top:197px;width:350px">Lorem ipsum dolor sit amet, consectetur adipiscing elit, sed diam nonummy nibh euismod tincidunt ut laoreet dolore magna aliquam erat volutpat. Lorem ipsum dolor sit amet, consectetur adipiscing elit, sed diam nonummy nibh euismod tincidunt ut laoreet dolore magna aliquam erat volutpat. Lorem ipsum dolor sit amet, consectetur adipiscing elit, sed diam nonummy nibh euismod tincidunt ut laoreet dolore magna aliquam erat volutpat.</div>
  <svg class="footer" viewBox="0 0 372 22"><rect y="2" width="372" height="20" fill="#3b3b3b"/><path d="M200 22C240 6 290 2 372 2V22Z" fill="#fff"/><path d="M200 22C240 6 290 2 372 2V5C300 5 250 10 218 22Z" fill="#0b48a6"/></svg>
  <div class="copyright">Copyright text here</div>
  <div class="brand">Bright Harbor Advisory</div>
</section>

<!-- Slide 10: thank you -->
<section class="slide" style="left:22px;top:902px">
  <div class="abs" style="left:0;top:0;width:372px;height:200px;background:var(--navy)"></div>
  <div class="abs" style="left:0;top:64px;width:372px;text-align:center;font:300 22px 'Montserrat',sans-serif;color:#fff;letter-spacing:.3px">THANKS YOU VERY MUCH</div>
  <div class="abs" style="left:0;top:122px;width:372px;text-align:center;font:400 11px 'Montserrat',sans-serif;color:#fff">Bright Harbor Advisory</div>
  <div class="abs" style="left:0;top:200px;width:372px;height:58px;background:#555"></div>
  <div class="abs" style="left:0;top:258px;width:372px;height:20px;background:#3b3b3b"></div>
  <div class="abs" style="left:6px;bottom:5px;color:#fff;font:600 4.6px 'Open Sans',sans-serif">Copyright text here</div>
  <svg class="abs" style="left:10px;top:222px" width="360" height="14" viewBox="0 0 360 14" fill="#0b48a6">
    <circle cx="6" cy="7" r="6"/><path d="M6 3.5a2 2 0 0 0-2 2c0 1.6 2 4 2 4s2-2.4 2-4a2 2 0 0 0-2-2z" fill="#fff"/>
    <circle cx="144" cy="7" r="6"/><path d="M141.5 4.5l1.2-.5 1 2-.8.6a4 4 0 0 0 1.8 1.8l.6-.8 2 1-.5 1.2c-2.5.2-5.6-2.8-5.3-5.3z" fill="#fff"/>
    <circle cx="272" cy="7" r="6"/><rect x="269" y="5" width="6" height="4" fill="#fff"/>
  </svg>
  <div class="abs" style="left:41px;top:221px;font:600 4.4px/5.2px 'Open Sans',sans-serif;color:#fff;letter-spacing:.4px">Your Address Here<br>Lorem Ipsum<br>Dolor Sit Amet</div>
  <div class="abs" style="left:167px;top:223px;font:600 4.4px/5.2px 'Open Sans',sans-serif;color:#fff;letter-spacing:.4px">Phone&nbsp; +01 234 56789<br>Fax&nbsp;&nbsp;&nbsp;&nbsp;&nbsp;&nbsp; +01 234 56789</div>
  <div class="abs" style="left:295px;top:223px;font:600 4.4px/5.2px 'Open Sans',sans-serif;color:#fff;letter-spacing:.4px">Email&nbsp; your@mail.com<br>Web&nbsp;&nbsp;&nbsp; www.company.com</div>
</section>

<!-- Slide 11: image titles + collage -->
<section class="slide" style="left:403px;top:902px">
  <div class="header">Project Title goes here</div>
  <div class="abs sub-title" style="left:12px;top:57px;font-size:8px">Image Title here</div>
  <div class="abs fine" style="left:12px;top:70px;width:190px">Lorem ipsum dolor sit amet, consectetur adipiscing elit, sed diam nonummy nibh euismod tincidunt ut laoreet dolore magna aliquam erat volutpat. Lorem ipsum dolor sit amet, consectetur adipiscing elit, sed diam nonummy nibh euismod tincidunt ut laoreet dolore magna aliquam erat volutpat. Lorem ipsum dolor sit amet, consectetur adipiscing elit, sed diam nonummy nibh euismod tincidunt ut laoreet dolore magna aliquam erat volutpat. Lorem ipsum dolor sit amet, consectetur adipiscing elit, sed diam nonummy nibh.</div>
  <div class="abs sub-title" style="left:12px;top:149px;font-size:8px">Image Title here</div>
  <div class="abs fine" style="left:12px;top:162px;width:190px">Lorem ipsum dolor sit amet, consectetur adipiscing elit, sed diam nonummy nibh euismod tincidunt ut laoreet dolore magna aliquam erat volutpat. Lorem ipsum dolor sit amet, consectetur adipiscing elit, sed diam nonummy nibh euismod tincidunt ut laoreet dolore magna aliquam erat volutpat. Lorem ipsum dolor sit amet, consectetur adipiscing elit, sed diam nonummy nibh euismod tincidunt ut laoreet dolore magna aliquam erat volutpat. Lorem ipsum dolor sit amet, consectetur adipiscing elit, sed diam nonummy nibh.</div>
  <div class="photo" role="img" aria-label="Collage of four photos showing hands using digital devices with technology icons" style="left:207px;top:53px;width:153px;height:197px;background:linear-gradient(150deg,#3e5f86 0%,#1d3457 45%,#0f1d33 100%)"></div>
  <svg class="footer" viewBox="0 0 372 22"><rect y="2" width="372" height="20" fill="#3b3b3b"/><path d="M200 22C240 6 290 2 372 2V22Z" fill="#fff"/><path d="M200 22C240 6 290 2 372 2V5C300 5 250 10 218 22Z" fill="#0b48a6"/></svg>
  <div class="copyright">Copyright text here</div>
  <div class="brand">Bright Harbor Advisory</div>
</section>

<!-- Slide 12: image placeholders + text -->
<section class="slide" style="left:790px;top:902px">
  <div class="header">Project Title goes here</div>
  <div class="abs" style="left:8px;top:53px;width:139px;height:81px;background:var(--pale)"></div>
  <div class="abs" style="left:8px;top:149px;width:139px;height:81px;background:var(--pale)"></div>
  <div class="abs sub-title" style="left:160px;top:52px;font-size:8px">Image Title here</div>
  <div class="abs fine" style="left:160px;top:65px;width:200px">Lorem ipsum dolor sit amet, consectetur adipiscing elit, sed diam nonummy nibh euismod tincidunt ut laoreet dolore magna aliquam erat volutpat. Lorem ipsum dolor sit amet, consectetur adipiscing elit, sed diam nonummy nibh euismod tincidunt ut laoreet dolore magna aliquam erat volutpat. Lorem ipsum dolor sit amet, consectetur adipiscing elit, sed diam nonummy nibh euismod tincidunt ut laoreet dolore magna aliquam erat volutpat.</div>
  <div class="abs sub-title" style="left:160px;top:145px;font-size:8px">Image Title here</div>
  <div class="abs fine" style="left:160px;top:158px;width:200px">Lorem ipsum dolor sit amet, consectetur adipiscing elit, sed diam nonummy nibh euismod tincidunt ut laoreet dolore magna aliquam erat volutpat. Lorem ipsum dolor sit amet, consectetur adipiscing elit, sed diam nonummy nibh euismod tincidunt ut laoreet dolore magna aliquam erat volutpat. Lorem ipsum dolor sit amet, consectetur adipiscing elit, sed diam nonummy nibh euismod tincidunt ut laoreet dolore magna aliquam erat volutpat.</div>
  <svg class="footer" viewBox="0 0 372 22"><rect y="2" width="372" height="20" fill="#3b3b3b"/><path d="M200 22C240 6 290 2 372 2V22Z" fill="#fff"/><path d="M200 22C240 6 290 2 372 2V5C300 5 250 10 218 22Z" fill="#0b48a6"/></svg>
  <div class="copyright">Copyright text here</div>
  <div class="brand">Bright Harbor Advisory</div>
</section>

</body>
</html>
```